Burn Cream

We need to develop a (1) tube and (2) carton design. For a Lidocaine 2.5% burn cream.

This is a topical application cream. KALVIO is the Product Name. 1 oz.

```html
<!DOCTYPE html>
<html lang="en">
<head>
<meta charset="utf-8">
<title>Kalvio Burn Cream – Tube Label</title>
<link href="https://fonts.googleapis.com/css2?family=Open+Sans:wght@400;600;700;800&display=swap" rel="stylesheet">
<style>
  :root {
    --stage: #eceef1;
    --label-light: #f4f9fd;
    --label-mid: #d7eaf8;
    --blue-bright: #3aa3e3;
    --blue-deep: #1f86cf;
    --brand-blue: #2a7fc4;
    --purple: #5a2d8c;
    --purple-soft: #6a3fa0;
    --ink: #1b1b1b;
    --rule: #2b2b2b;
    --green: #3b9a3b;
    --flag: #b8404a;
  }
  * { box-sizing: border-box; margin: 0; padding: 0; }
  html, body { width: 1200px; height: 1000px; overflow: hidden; }
  body {
    background: var(--stage);
    font-family: "Open Sans", Arial, sans-serif;
    color: var(--ink);
    position: relative;
  }
  .label {
    position: absolute;
    left: 60px;
    width: 1080px;
    height: 400px;
    overflow: hidden;
    background: linear-gradient(115deg, var(--label-light) 0%, #ffffff 40%, var(--label-mid) 100%);
    box-shadow: 0 2px 10px rgba(0,0,0,.12);
  }
  .label--front { top: 60px; }
  .label--back { top: 540px; }
  .label__facets { position: absolute; inset: 0; width: 100%; height: 100%; }

  /* Front */
  .maker {
    position: absolute; left: 120px; top: 96px;
    font-weight: 700; font-size: 18px; color: var(--brand-blue);
    letter-spacing: .5px;
  }
  .product-name {
    position: absolute; left: 112px; top: 112px;
    font-weight: 800; font-size: 118px; line-height: 1;
    color: var(--purple); letter-spacing: -3px;
  }
  .product-type {
    position: absolute; left: 240px; top: 238px;
    font-weight: 700; font-size: 44px; color: var(--purple-soft);
  }
  .tagline {
    position: absolute; left: 128px; top: 300px;
    font-weight: 700; font-size: 22px; color: var(--ink);
  }
  .benefits {
    position: absolute; left: 640px; top: 120px;
    list-style: none;
  }
  .benefits li {
    display: flex; align-items: center; gap: 14px;
    font-weight: 600; font-size: 23px; margin-bottom: 22px;
  }
  .benefits svg { width: 34px; height: 30px; flex: none; }
  .info-box {
    position: absolute; left: 640px; top: 24px;
    width: 300px; height: 44px;
    border: 1px solid #9fb3c2;
  }

  /* Back */
  .drug-facts {
    position: absolute; left: 110px; top: 40px;
    width: 360px; border: 2px solid var(--rule);
    font-size: 11px; background: rgba(255,255,255,.7);
  }
  .drug-facts__title { font-weight: 800; font-size: 17px; padding: 4px 8px; border-bottom: 3px solid var(--rule); }
  .drug-facts__row { display: flex; justify-content: space-between; padding: 5px 8px; border-bottom: 1px solid var(--rule); }
  .drug-facts__row:last-child { border-bottom: 0; }
  .drug-facts__row b { font-weight: 700; }
  .maker-block {
    position: absolute; left: 110px; top: 250px;
    font-size: 12px; line-height: 1.45;
  }
  .maker-block .maker-name { font-weight: 700; font-size: 17px; color: var(--brand-blue); margin-bottom: 4px; }
  .marks {
    position: absolute; left: 360px; top: 270px;
    display: flex; gap: 26px; align-items: flex-end;
    font-size: 10px; font-weight: 700; text-align: center;
  }
  .marks .flag { width: 34px; height: 22px; background: var(--flag); margin: 0 auto 4px; }
  .copy {
    position: absolute; left: 540px; top: 44px; width: 430px;
    font-size: 15px; line-height: 1.55; color: var(--ink);
  }
  .copy p + p { margin-top: 12px; }
</style>
</head>
<body>

<section class="label label--front" aria-label="Tube front label">
  <svg class="label__facets" viewBox="0 0 1080 400" preserveAspectRatio="none" aria-hidden="true">
    <polygon points="0,0 70,0 40,400 0,400" fill="var(--blue-bright)" opacity=".85"/>
    <polygon points="70,0 180,0 40,400" fill="var(--blue-deep)" opacity=".25"/>
    <polygon points="1080,0 960,0 1080,260" fill="var(--blue-bright)" opacity=".85"/>
    <polygon points="960,0 880,0 1080,400 1080,260" fill="var(--blue-deep)" opacity=".2"/>
    <polygon points="300,400 620,180 760,400" fill="#bcdcf3" opacity=".35"/>
    <polygon points="520,0 760,0 640,210" fill="#cfe6f7" opacity=".4"/>
  </svg>
  <div class="info-box"></div>
  <div class="maker">VERDALUX</div>
  <div class="product-name">KALVIO</div>
  <div class="product-type">BURN CREAM</div>
  <div class="tagline">For Immediate Burn Treatment</div>
  <ul class="benefits">
    <li><svg viewBox="0 0 34 30"><path d="M2 16 L12 27 L32 2" fill="none" stroke="var(--ink)" stroke-width="3.5"/></svg>Fast Acting</li>
    <li><svg viewBox="0 0 34 30"><path d="M2 16 L12 27 L32 2" fill="none" stroke="var(--ink)" stroke-width="3.5"/></svg>Relieve Pain From Burns</li>
    <li><svg viewBox="0 0 34 30"><path d="M2 16 L12 27 L32 2" fill="none" stroke="var(--ink)" stroke-width="3.5"/></svg>Treats Skin Abrasions</li>
  </ul>
</section>

<section class="label label--back" aria-label="Tube back label">
  <svg class="label__facets" viewBox="0 0 1080 400" preserveAspectRatio="none" aria-hidden="true">
    <polygon points="0,0 70,0 40,400 0,400" fill="var(--blue-bright)" opacity=".85"/>
    <polygon points="1080,0 990,0 1080,200" fill="var(--blue-bright)" opacity=".85"/>
    <polygon points="480,400 700,120 900,400" fill="#bcdcf3" opacity=".35"/>
    <polygon points="780,0 1000,0 900,160" fill="#cfe6f7" opacity=".4"/>
  </svg>
  <div class="drug-facts">
    <div class="drug-facts__title">Drug Facts</div>
    <div class="drug-facts__row"><span><b>Active ingredient</b> Lidocaine 2.5%</span><span><b>Purpose</b> Topical analgesic</span></div>
    <div class="drug-facts__row"><span><b>Uses</b> temporarily relieves pain of minor burns</span></div>
    <div class="drug-facts__row"><span><b>Warnings</b> For external use only</span></div>
    <div class="drug-facts__row"><span><b>Directions</b> apply a thin layer up to 3 times daily</span></div>
  </div>
  <div class="maker-block">
    <div class="maker-name">VERDALUX</div>
    Manufactured by:<br>
    Verdalux Ltd<br>
    12 Harlow Street<br>
    Brookfield, MA 01506<br>
    United States<br>
    +1 555 014 2270<br>
    info@verdalux-care.com
  </div>
  <div class="marks">
    <div>
      <svg width="30" height="28" viewBox="0 0 30 28" aria-hidden="true"><path d="M15 2 L27 24 L3 24 Z" fill="none" stroke="var(--green)" stroke-width="3"/></svg>
      <div>RECYCLE</div>
    </div>
    <div>
      <div class="flag" role="img" aria-label="National flag"></div>
      <div>MADE IN USA</div>
    </div>
  </div>
  <div class="copy">
    <p>Lorem ipsum dolor sit amet, consectetur adipiscing elit. Cras in lorem ut quis ante luctus laoreet sit amet vel turpis. Quisque ornare gravida nisl quis tristique.</p>
    <p>Nulla ullamcorper metus sit amet ipsum rhoncus, eu pharetra risus facilisis. Phasellus tristique consectetur leo, vitae rutrum ipsum. Vestibulum ante ipsum primis in faucibus.</p>
    <p>Curabitur posuere cubilia curae; aenean ligula metus, ornare sed metus ut, commodo maximus lectus.</p>
  </div>
</section>

</body>
</html>
```